Humor Novelist needs a warm, playful cover

I need a cover for my Lumora ebook and 5 x 8 paperback, Braver as Sasquatches: A Farce. It’s a humor novel set in America’s heartland about a guy fresh out of college who stumbles onto a town full of werewolves. It’s funny but not wacky—a paranormal coming of age story. Should be cheeky but not look like pie-in-the-face humor.

FRONT COVER should include:

Braver as Sasquatches: A Farce
Dominic Pellworth

BACK COVER should include:

Dominic Pellworth

Fresh out of college and armed with a research grant, Milo Vantrask heads to the backwoods of his home state to look for Bigfoot. While camping near his grandfather’s vineyard he learns that the forest is populated by wolves—unusually clever ones. He discovers a nearby town where malt shops, milkmen, and the 1950’s never stopped. Along with his lecherous grandfather and mysterious girlfriend, Milo must navigate wolfmen and gun-toting rednecks to discover the secret uniting an entire town to werewolves.

“Probably the funniest paranormal coming of age novel to come out since that awful paperback about shiny vampires with mood swings.”
– The Meridian Trumpet

“None of the awkward sex scenes in this book indicate that Dominic Pellworth has ever actually had sex. I liked the stuff about werewolves, though.”
– The Hollowmere Ledger

“Reads like Beaumont Trelawny retelling something Morton Quayle cranked out before he sobered up.”
– Galloway Critiques

Target Market(s)

Adult comedy readers

Industry/Entity Type

Book Publisher

Font styles to use
Serif

Colors
0292cd
33a6d7
85cae6
86cfc6
33b8a4
00a990
0255a3
3276b5
85abd2

Requirements
Must have
• (on the front) Author Name, Title (on the back) Synopsis and reviews
Should not have
• A horror feel to it, romance cover feel to it

```html
<!DOCTYPE html>
<html lang="en">
<head>
<meta charset="utf-8">
<title>Braver as Sasquatches: A Farce</title>
<link rel="stylesheet" href="https://fonts.googleapis.com/css2?family=Questrial&family=EB+Garamond:ital@0;1&display=swap">
<style>
  :root {
    --cover-sea: #a3d6d6;
    --cover-sea-low: #add9e0;
    --spine-paper: #f1f6f4;
    --title-white: #f7f9f6;
    --spine-title: #8ccfcf;
    --rust: #9b5c42;
    --quote-red: #b33429;
    --art-light: #e9f1ee;
    --art-rust: #b77a5a;
  }
  html, body { margin: 0; padding: 0; overflow: hidden; }
  body { width: 1200px; height: 909px; }
  .jacket {
    position: relative; width: 1200px; height: 909px; overflow: hidden;
    background: linear-gradient(180deg, var(--cover-sea) 0%, var(--cover-sea) 75%, var(--cover-sea-low) 100%);
    font-family: "EB Garamond", Georgia, serif;
  }
  .display {
    font-family: "Questrial", Arial, sans-serif; font-weight: 400;
  }

  /* Back cover */
  .back { position: absolute; left: 0; top: 0; width: 568px; height: 909px; }
  .back-heading {
    position: absolute; left: 0; width: 568px; text-align: center;
    color: var(--title-white); margin: 0;
    -webkit-text-stroke: 0.7px var(--title-white);
  }
  .back-title { top: 52px; font-size: 25px; letter-spacing: 0.5px; }
  .back-author { top: 84px; font-size: 18px; letter-spacing: 0.5px; }
  .review {
    position: absolute; left: 100px; width: 368px; margin: 0; text-align: center;
    color: var(--quote-red); font-size: 16.6px; line-height: 26px;
  }
  .review cite { display: block; color: var(--title-white); font-style: italic; }
  .review-one { top: 132px; }
  .review-two { top: 262px; }
  .review-three { top: 392px; }
  .synopsis {
    position: absolute; left: 71px; top: 496px; width: 426px; margin: 0;
    color: var(--quote-red); font-size: 17px; line-height: 26px;
    letter-spacing: 0.15px; text-align: justify; hyphens: auto;
  }

  /* Spine */
  .spine {
    position: absolute; left: 568px; top: 0; width: 64px; height: 909px;
    background: var(--spine-paper);
  }
  .spine-author {
    position: absolute; left: 12px; top: 32px; margin: 0;
    writing-mode: vertical-rl; color: var(--rust);
    font-size: 19px; line-height: 20px;
    -webkit-text-stroke: 0.6px var(--rust);
  }
  .spine-title {
    position: absolute; left: 6px; top: 160px; margin: 0;
    writing-mode: vertical-rl; color: var(--spine-title);
    font-size: 50px; line-height: 52px; letter-spacing: 4px;
    white-space: nowrap;
    -webkit-text-stroke: 1px var(--spine-title);
  }

  /* Front cover */
  .front { position: absolute; left: 632px; top: 0; width: 568px; height: 909px; }
  .front-title {
    position: absolute; left: 28px; top: 14px; margin: 0;
    color: var(--title-white); line-height: 1;
    -webkit-text-stroke: 2px var(--title-white);
  }
  .front-title span { display: block; }
  .line-braver { font-size: 118px; height: 110px; }
  .line-as { font-size: 118px; height: 112px; }
  .line-sas { font-size: 118px; height: 108px; }
  .line-quatches { font-size: 98px; letter-spacing: -1px; }
  .genre-tag {
    position: absolute; left: 274px; top: 166px; margin: 0;
    color: var(--rust); font-size: 36px; letter-spacing: 0.5px;
    -webkit-text-stroke: 1.2px var(--rust);
  }
  .cover-art { position: absolute; left: 14px; top: 466px; width: 522px; height: 204px; }
  .front-author {
    position: absolute; right: 58px; top: 708px; margin: 0; text-align: right;
    color: var(--title-white); line-height: 1;
    -webkit-text-stroke: 2px var(--title-white);
  }
  .front-author span { display: block; }
  .author-first { font-size: 72px; height: 80px; }
  .author-last { font-size: 84px; }
</style>
</head>
<body>
<main class="jacket">
  <section class="back">
    <h2 class="back-heading back-title display">BRAVER AS SASQUATCHES</h2>
    <p class="back-heading back-author display">DOMINIC PELLWORTH</p>

    <blockquote class="review review-one">
      “Probably the funniest paranormal coming of age novel to come out since that awful paperback about shiny vampires with mood swings.”
      <cite>– The Meridian Trumpet</cite>
    </blockquote>
    <blockquote class="review review-two">
      “None of the awkward sex scenes in this book indicate that Dominic Pellworth has ever actually had sex. I liked the stuff about werewolves, though.”
      <cite>– The Hollowmere Ledger</cite>
    </blockquote>
    <blockquote class="review review-three">
      “Reads like Beaumont Trelawny retelling something Morton Quayle cranked out before he sobered up.”
      <cite>– Galloway Critiques</cite>
    </blockquote>

    <p class="synopsis">Fresh out of college and armed with a research grant, Milo Vantrask heads to the backwoods of his home state to look for Bigfoot. While camping near his grandfather’s vineyard he learns that the forest is populated by wolves—unusually clever ones. He discovers a nearby town where malt shops, milkmen, and the 1950’s never stopped. Along with his lecherous grandfather and mysterious girlfriend, Milo must navigate wolfmen and gun-toting rednecks to discover the secret uniting an entire town to werewolves.</p>
  </section>

  <section class="spine">
    <p class="spine-author display">DOMINIC<br>PELLWORTH</p>
    <h2 class="spine-title display">BRAVER AS SASQUATCHES</h2>
  </section>

  <section class="front">
    <h1 class="front-title display">
      <span class="line-braver">BRAVER</span>
      <span class="line-as">AS</span>
      <span class="line-sas">SAS–</span>
      <span class="line-quatches">QUATCHES</span>
    </h1>
    <p class="genre-tag display">A FARCE</p>

    <svg class="cover-art" viewBox="0 0 522 204" role="img" aria-label="Illustration: a pair of mismatched wide cartoon eyes, one bloodshot under a jagged shock of rust-coloured hair, the other calm under a thin raised brow">
      <defs>
        <linearGradient id="artTone" x1="0" y1="0" x2="1" y2="0">
          <stop offset="0" stop-color="var(--art-rust)" stop-opacity="0.35"/>
          <stop offset="0.5" stop-color="var(--art-light)" stop-opacity="0.55"/>
          <stop offset="1" stop-color="var(--art-light)" stop-opacity="0.45"/>
        </linearGradient>
      </defs>
      <rect x="0" y="0" width="522" height="204" fill="url(#artTone)"/>
    </svg>

    <h2 class="front-author display">
      <span class="author-first">DOMINIC</span>
      <span class="author-last">PELLWORTH</span>
    </h2>
  </section>
</main>
</body>
</html>
```